Larder & Flame - Premium Catering needs a new menu design.

I currently use menupro to make my own menus for printing and uploading to the website (PDF). I need a professional menu to replace my current menu. I wold like to mail these menus out so I'm thinking a tri-fold menu would be the best option. Similar to what pizzerias send out.

Logo Text

Would be good to reduce the text thickness of the letters "MIL" in the word MILLRUN. Right now MIL has thicker text.

Colors

Designer to choose colors to be used in the design.

```html
<!DOCTYPE html>
<html lang="en">
<head>
<meta charset="utf-8">
<title>Millrun Larder &amp; Flame – Menu</title>
<link href="https://fonts.googleapis.com/css2?family=Oswald:wght@400;500;700&family=Didact+Gothic&display=swap" rel="stylesheet">
<style>
  :root {
    --paper: #ffffff;
    --board-light: #3b3b3b;
    --board-dark: #202020;
    --chalk: #ffffff;
    --mustard: #e8bb4a;
    --heading-font: "Oswald", sans-serif;
    --item-font: "Didact Gothic", sans-serif;
  }
  * { box-sizing: border-box; margin: 0; padding: 0; }
  html, body { width: 1200px; height: 800px; overflow: hidden; background: var(--paper); }
  .canvas { position: relative; width: 1200px; height: 800px; }

  .page {
    position: absolute; width: 514px; height: 730px;
    background: radial-gradient(ellipse at 50% 48%, var(--board-light) 0%, #2c2c2c 55%, var(--board-dark) 100%);
    box-shadow: 6px 10px 22px rgba(0,0,0,.35);
    color: var(--chalk);
  }
  .page--cover { left: 66px; top: 37px; }
  .page--menu { left: 633px; top: 36px; }

  .brush { position: absolute; background: var(--mustard); border-radius: 3px; }
  .menu-title {
    position: absolute; font-family: var(--heading-font); font-weight: 700;
    color: var(--chalk); line-height: 1; letter-spacing: 1px; text-align: center;
  }
  .page--cover .brush { left: 92px; top: 64px; width: 330px; height: 80px; }
  .page--cover .menu-title { left: 0; width: 514px; top: 46px; font-size: 126px; transform: scaleY(1.0); }
  .page--menu .brush { left: 170px; top: 50px; width: 172px; height: 42px; }
  .page--menu .menu-title { left: 0; width: 514px; top: 35px; font-size: 70px; }

  .brand-mark { position: absolute; border: 2px solid var(--mustard); border-radius: 50%; }
  .page--cover .brand-mark { left: 232px; top: 268px; width: 50px; height: 50px; }
  .page--menu .brand-mark { left: 245px; top: 630px; width: 20px; height: 20px; }

  .brand { position: absolute; left: 0; width: 514px; text-align: center;
    font-family: var(--heading-font); font-weight: 500; color: var(--chalk); }
  .brand__name, .brand__line { display: block; line-height: 1; }
  .page--cover .brand { top: 362px; }
  .page--cover .brand__name { font-size: 52px; letter-spacing: 3px; }
  .page--cover .brand__line--a { font-size: 29px; letter-spacing: 3px; margin-top: 12px; }
  .page--cover .brand__line--b { font-size: 25px; letter-spacing: 3px; margin-top: 8px; }
  .page--menu .brand { top: 658px; }
  .page--menu .brand__name { font-size: 18px; letter-spacing: 1px; }
  .page--menu .brand__line--a { font-size: 10px; letter-spacing: 1px; margin-top: 2px; }
  .page--menu .brand__line--b { font-size: 8px; letter-spacing: 1px; margin-top: 2px; }

  .contact { position: absolute; left: 0; width: 514px; text-align: center;
    font-family: var(--heading-font); font-weight: 400; color: var(--chalk); line-height: 1; }
  .contact--site { top: 562px; font-size: 14px; letter-spacing: 4.5px; }
  .contact--address { top: 587px; font-size: 16px; letter-spacing: 4.5px; }
  .contact-rule { position: absolute; left: 177px; top: 616px; width: 159px; height: 2px; background: var(--chalk); }
  .contact--delivery { top: 633px; font-size: 15px; letter-spacing: 4.5px; }
  .contact--hours { top: 682px; font-size: 14px; letter-spacing: 4.5px; }

  .section-frame { position: absolute; left: 40px; width: 433px; }
  .section-frame svg { position: absolute; left: 0; top: 0; }
  .section-frame--starters { top: 136px; height: 135px; }
  .section-frame--drinks { top: 469px; height: 132px; }
  .section-label {
    position: absolute; left: 168px; top: 0; width: 89px; height: 33px;
    border: 1.5px solid var(--chalk); text-align: center;
    font-family: var(--heading-font); font-weight: 500; font-size: 24px; line-height: 30px;
  }

  .items { position: absolute; list-style: none; font-family: var(--item-font);
    color: var(--chalk); font-size: 12.5px; }
  .items li { display: flex; justify-content: space-between; height: 17px; line-height: 17px; }
  .items--burgers li, .items--desserts li { height: 19.2px; line-height: 19.2px; font-size: 13px; }
  .items--drinks li { height: 19px; line-height: 19px; font-size: 13px; }

  .col-divider { position: absolute; width: 1.5px; background: var(--chalk); }

  .group-heading { position: absolute; font-family: var(--heading-font); font-weight: 500;
    font-size: 25px; line-height: 1; color: var(--chalk); }
</style>
</head>
<body>
<main class="canvas">

  <section class="page page--cover">
    <div class="brush" role="img" aria-label="Mustard-yellow paint brush stroke behind the title"></div>
    <h1 class="menu-title">MENU</h1>
    <div class="brand-mark"></div>
    <p class="brand">
      <span class="brand__name">MILLRUN</span>
      <span class="brand__line brand__line--a">LARDER &amp; FLAME</span>
      <span class="brand__line brand__line--b">PREMIUM CATERING</span>
    </p>
    <p class="contact contact--site">MILLRUNLARDER&amp;FLAME</p>
    <p class="contact contact--address">14 ROUTE 9 ALDER FALLS, NJ 08123</p>
    <div class="contact-rule"></div>
    <p class="contact contact--delivery">DELIVERY: MILLRUNLARDER.COM</p>
    <p class="contact contact--hours">OPEN DAILY AND ON MOST HOLIDAYS</p>
  </section>

  <section class="page page--menu">
    <div class="brush" role="img" aria-label="Mustard-yellow paint brush stroke behind the title"></div>
    <h2 class="menu-title">MENU</h2>

    <div class="section-frame section-frame--starters">
      <svg width="433" height="135" viewBox="0 0 433 135" aria-hidden="true">
        <polyline points="131,16 1.5,16 1.5,133.5 431.5,133.5 431.5,16 294,16" fill="none" stroke="#fff" stroke-width="2.5"/>
      </svg>
      <div class="section-label">STARTERS</div>
    </div>
    <ul class="items" style="left:67px; top:196px; width:166px;">
      <li><span>DELICIOUS STARTER</span><span>13.00 $</span></li>
      <li><span>TO SHARE</span><span>7.00 $</span></li>
      <li><span>BEST OPTION</span><span>9.00 $</span></li>
    </ul>
    <div class="col-divider" style="left:256px; top:186px; height:62px;"></div>
    <ul class="items" style="left:281px; top:196px; width:165px;">
      <li><span>STARTER 1 RICE</span><span>11.00 $</span></li>
      <li><span>STARTER 2 GRILL</span><span>16.00 $</span></li>
      <li><span>STARTER 3 MEX</span><span>16.00 $</span></li>
    </ul>

    <h3 class="group-heading" style="left:51px; top:300px;">BURGERS</h3>
    <ul class="items items--burgers" style="left:50px; top:342px; width:180px;">
      <li><span>DELICIOUS MEAT</span><span>14.00 $</span></li>
      <li><span>BEST BURGUER</span><span>13.50 $</span></li>
      <li><span>AUTHENTIC GRILL</span><span>12.00 $</span></li>
      <li><span>BBQ MEAT</span><span>14.80 $</span></li>
      <li><span>BEST TASTE</span><span>13.50 $</span></li>
    </ul>

    <h3 class="group-heading" style="right:52px; top:303px;">DESERTS</h3>
    <ul class="items items--desserts" style="left:289px; top:345px; width:170px;">
      <li><span>BROWNIE</span><span>4.50 $</span></li>
      <li><span>BEST CHEESECAKE</span><span>6.00 $</span></li>
      <li><span>CARROT CAKE</span><span>5.00 $</span></li>
      <li><span>CHOCOLATE</span><span>3.00 $</span></li>
      <li><span>APPLE PIE</span><span>6.00 $</span></li>
    </ul>

    <div class="section-frame section-frame--drinks">
      <svg width="433" height="132" viewBox="0 0 433 132" aria-hidden="true">
        <polyline points="131,16 1.5,16 1.5,130.5 431.5,130.5 431.5,16 294,16" fill="none" stroke="#fff" stroke-width="2.5"/>
      </svg>
      <div class="section-label">DRINKS</div>
    </div>
    <ul class="items items--drinks" style="left:67px; top:518px; width:168px;">
      <li><span>WATER</span><span>2.00 $</span></li>
      <li><span>BEER</span><span>3.00 $</span></li>
      <li><span>COCKTAIL</span><span>8.00 $</span></li>
    </ul>
    <div class="col-divider" style="left:254px; top:517px; height:62px;"></div>
    <ul class="items items--drinks" style="left:278px; top:518px; width:168px;">
      <li><span>TONIC</span><span>2.00 $</span></li>
      <li><span>BEER 0,0</span><span>3.00 $</span></li>
      <li><span>DRINKS</span><span>3.00 $</span></li>
    </ul>

    <div class="brand-mark"></div>
    <p class="brand">
      <span class="brand__name">MILLRUN</span>
      <span class="brand__line brand__line--a">LARDER &amp; FLAME</span>
      <span class="brand__line brand__line--b">PREMIUM CATERING</span>
    </p>
  </section>

</main>
</body>
</html>
```